nukh almasira
nukh almasira - Corporate Services
Creative Brief
Simple
Kadhim Rubaie كاظم الربيعي
CEO المدير المفوض
Locality 482 - Alley 17 - House 8 Al Mansour - Baghdad - Iraq محلة 482 - زقاق 17 - دار 8 المنصور - بغداد - العراق
CEO@nukhalmasira.example
www.nukhalmasira.example
Concepts
Business Cards and Stationery for new compliance company.
Business Cards and Stationery for Background Check Company
qorvel42 qorvel42
good design but i hope you use the same name and information in the brief and if you can work on the logo cause i want to add the Arabic name of the company ( نخبة المسيرة ) if you can put the logo in the left and the name of the company in English and Arabic in the right of the logo and use the same font and size in Arabic and English name
Brisk Brisk
Ok
Please show me the whole stationary not only the business card
please use this e-mail on the letterhead only info@nukhalmasira.example and the address in arabic language use it only in the letterhead too thankyou

```html
<!DOCTYPE html>
<html lang="en">
<head>
<meta charset="utf-8">
<title>nukh almasira – Business Card</title>
<link href="https://fonts.googleapis.com/css2?family=Raleway:wght@400;500;600;700&display=swap" rel="stylesheet">
<style>
  :root {
    --brand-blue: #3a8fd4;
    --brand-blue-dark: #2a78b9;
    --brand-orange: #f5a623;
    --paper: #ffffff;
    --stage: #e9ebee;
    --ink-light: #ffffff;
  }
  * { box-sizing: border-box; margin: 0; padding: 0; }
  html, body {
    width: 1200px; height: 901px; overflow: hidden;
    background: var(--stage);
    font-family: "Raleway", sans-serif;
  }
  .stage {
    position: relative; width: 1200px; height: 901px;
    display: flex; align-items: center; justify-content: center; gap: 40px;
  }
  .card {
    position: relative; width: 540px; height: 310px;
    border-radius: 24px; overflow: hidden;
    box-shadow: 0 10px 24px rgba(0,0,0,0.15);
  }
  .card-bg { position: absolute; inset: 0; width: 100%; height: 100%; }

  /* front */
  .brand {
    position: absolute; display: flex; align-items: center; gap: 10px;
  }
  .brand-front { left: 34px; top: 38px; }
  .brand-dot {
    width: 34px; height: 34px; border-radius: 50%;
    background: var(--brand-orange);
  }
  .brand-name {
    font-weight: 600; font-size: 24px; letter-spacing: 1.5px;
    text-transform: uppercase; color: var(--brand-blue);
  }
  .holder {
    position: absolute; left: 34px; top: 196px; color: var(--ink-light);
  }
  .holder-name {
    font-size: 15px; font-weight: 700; letter-spacing: 1px; text-transform: uppercase;
  }
  .holder-title { font-size: 11px; font-weight: 500; margin-top: 2px; }
  .holder-address { font-size: 11px; line-height: 1.45; margin-top: 14px; }

  .contacts {
    position: absolute; right: 30px; top: 170px; list-style: none;
    color: var(--ink-light); font-size: 11px; font-weight: 500;
    display: flex; flex-direction: column; gap: 7px; align-items: flex-end;
  }
  .contacts li { display: flex; align-items: center; gap: 8px; }
  .contacts svg { width: 12px; height: 12px; fill: var(--ink-light); }

  /* back */
  .card-back { background: var(--brand-blue); }
  .brand-back { left: 50%; top: 50%; transform: translate(-50%, -50%); }
  .brand-back .brand-dot { background: var(--brand-orange); width: 40px; height: 40px; }
  .brand-back .brand-name { color: var(--ink-light); font-size: 26px; }
</style>
</head>
<body>
<main class="stage">
  <section class="card card-front" aria-label="Business card front">
    <svg class="card-bg" viewBox="0 0 540 310" preserveAspectRatio="none" aria-hidden="true">
      <rect width="540" height="310" fill="var(--brand-blue)"/>
      <path d="M0 0 H540 V172 C440 182 350 160 260 128 C170 98 80 96 0 126 Z" fill="var(--brand-orange)"/>
      <path d="M0 0 H540 V160 C440 170 350 148 260 116 C170 86 80 84 0 114 Z" fill="var(--paper)"/>
    </svg>

    <div class="brand brand-front">
      <span class="brand-dot"></span>
      <span class="brand-name">nukh almasira</span>
    </div>

    <div class="holder">
      <p class="holder-name">Kadhim Rubaie</p>
      <p class="holder-title">Managing Director</p>
      <p class="holder-address">Locality 482 - Alley 17<br>House 8 Al Mansour</p>
    </div>

    <ul class="contacts">
      <li>012 345 6789
        <svg viewBox="0 0 24 24"><path d="M6.6 10.8a15.1 15.1 0 0 0 6.6 6.6l2.2-2.2c.3-.3.7-.4 1-.2 1.1.4 2.3.6 3.6.6.6 0 1 .4 1 1V20c0 .6-.4 1-1 1C10.6 21 3 13.4 3 4c0-.6.4-1 1-1h3.5c.6 0 1 .4 1 1 0 1.3.2 2.5.6 3.6.1.3 0 .7-.2 1z"/></svg></li>
      <li>012 345 6789
        <svg viewBox="0 0 24 24"><path d="M4 5h16v10H4zM2 17h20v2H2z"/></svg></li>
      <li>012 345 6789
        <svg viewBox="0 0 24 24"><path d="M7 2h10a1 1 0 0 1 1 1v18a1 1 0 0 1-1 1H7a1 1 0 0 1-1-1V3a1 1 0 0 1 1-1zm1 3v13h8V5z"/></svg></li>
      <li>CEO@nukhalmasira.example
        <svg viewBox="0 0 24 24"><path d="M2 5h20v14H2zm2 2v.5l8 5 8-5V7l-8 5z"/></svg></li>
      <li>www.nukhalmasira.example
        <svg viewBox="0 0 24 24"><path d="M12 2a10 10 0 1 0 0 20 10 10 0 0 0 0-20zm0 2c1.2 1.5 2 3.6 2.2 7H9.8C10 7.6 10.8 5.5 12 4zM4.1 13h3.7c.1 2.4.6 4.4 1.4 6A8 8 0 0 1 4.1 13zm0-2A8 8 0 0 1 9.2 5c-.8 1.6-1.3 3.6-1.4 6zm5.7 2h4.4c-.2 3.4-1 5.5-2.2 7-1.2-1.5-2-3.6-2.2-7zm5 6c.8-1.6 1.3-3.6 1.4-6h3.7a8 8 0 0 1-5.1 6zm1.4-8c-.1-2.4-.6-4.4-1.4-6a8 8 0 0 1 5.1 6z"/></svg></li>
    </ul>
  </section>

  <section class="card card-back" aria-label="Business card back">
    <div class="brand brand-back">
      <span class="brand-dot"></span>
      <span class="brand-name">nukh almasira</span>
    </div>
  </section>
</main>
</body>
</html>
```